Fall Festival & Movie Night

This is small church that is reaching out to the community to spread the gospel. We are having a free food, drinks, games and a free movie. I want the post card to read:
Free Food & Drinks
Free Games
Free Movie - Rivers Still Run
When: Saturday, October 11th
Games and Food start at 4:00 pm
Movie starts at 6:15 pm
Where: 4619 Marlow Lane South Chesterfield - Future Home of Brookhaven Fellowship Church
Rain Date: October 18th
Updates
To all designers:
Thank you so much for your hard work and creative postcards. We have decided to go with design #4544179 from designer "tarnwick". This designer has illustrated and captured the feel of our event from the very beginning and we are very pleased to go with that design. It still has a couple last minute details so this project remains open; however, as a courtesy do not submit any more designs as to not "waste" your very valuable time.
Once again many thanks. :)
Industry/Entity Type
Church
Font styles to use
Requirements
Must have
- Have oversized post cards in possession by October 3rd. Please send in designs as soon as possible.
Nice to have
- Country Background (open grassy area, with trees outlining property. location is Chesterfield, Virginia). three wooden crosses would be nice. also people talking and eating on grassy area would work.

```html
<!DOCTYPE html>
<html lang="en">
<head>
<meta charset="UTF-8">
<title>Fall Festival &amp; Movie Night Postcard</title>
<link rel="stylesheet" href="https://fonts.googleapis.com/css2?family=Lobster&family=Open+Sans:ital,wght@0,400;0,700;1,700&display=swap">
<style>
  :root {
    --bg: #ece6dc;
    --lime: #9bcb3b;
    --lime-deep: #86bc2a;
    --cream: #f6f1dc;
    --blue: #1d5fa8;
    --navy: #1f3c8a;
    --sky: #2a8fd0;
    --red: #e8404a;
    --orange: #f0a142;
    --white: #ffffff;
    --ink: #333333;
    --rule: #b9b9b9;
  }
  * { box-sizing: border-box; margin: 0; padding: 0; }
  html, body { width: 1200px; height: 500px; overflow: hidden; }
  body {
    position: relative;
    background: var(--bg);
    font-family: "Open Sans", Arial, sans-serif;
  }

  /* Front of card */
  .card-front {
    position: absolute; left: 27px; top: 33px; width: 558px; height: 430px;
    border: 6px solid var(--lime);
    background: linear-gradient(90deg, var(--cream) 0%, #dfe9a6 45%, var(--lime) 100%);
    overflow: hidden;
  }
  .title {
    position: absolute; left: 26px; top: 4px;
    font-family: "Lobster", cursive; font-size: 43px; font-weight: 400; color: var(--blue);
    text-shadow: 2px 2px 0 var(--white); white-space: nowrap; letter-spacing: 0.3px;
  }
  .enjoy {
    position: absolute; left: 22px; top: 68px;
    font-family: "Lobster", cursive; font-size: 27px; color: var(--sky);
  }
  .offers {
    position: absolute; left: 22px; top: 106px; width: 166px;
    font-size: 13px; line-height: 18px; color: var(--navy); white-space: nowrap;
  }
  .offers .lead { font-weight: 700; }
  .offers .detail { font-style: italic; font-size: 12.5px; }
  .offers .movie { font-weight: 700; color: var(--sky); }
  .offers .movie-title { font-weight: 700; color: var(--red); text-transform: uppercase; padding-left: 14px; margin-top: 2px; }
  .offers .movie-time { font-weight: 700; color: var(--sky); padding-left: 16px; margin-top: 2px; }
  .event-photo {
    position: absolute; left: 192px; top: 48px; width: 352px; height: 254px;
    background: linear-gradient(180deg, #4f7a3a 0%, #6c9a46 40%, #5e9a3c 100%);
  }
  .crosses {
    position: absolute; left: 28px; top: 252px; width: 90px; height: 168px;
    background: linear-gradient(180deg, rgba(120,80,50,0.35), rgba(120,80,50,0.15));
  }
  .details {
    position: absolute; left: 120px; top: 306px; list-style: none;
    font-size: 13.5px; line-height: 19px; font-weight: 700; color: var(--navy); white-space: nowrap;
  }
  .details li { position: relative; padding-left: 14px; }
  .details li::before {
    content: ""; position: absolute; left: 0; top: 5px;
    width: 10px; height: 10px; border-radius: 50%; background: var(--red);
  }
  .details li.cont::before { display: none; }
  .bring {
    position: absolute; left: 170px; top: 384px; width: 290px; text-align: center;
    font-size: 12px; line-height: 14px; font-style: italic; font-weight: 700; color: var(--red);
  }

  /* Back of card */
  .card-back {
    position: absolute; left: 613px; top: 33px; width: 560px; height: 432px;
    background: var(--white);
  }
  .welcome-panel {
    position: absolute; left: 0; top: 0; width: 270px; height: 355px;
    border: 6px solid var(--orange); background: var(--lime-deep);
  }
  .picnic-photo {
    position: absolute; left: 0; top: 0; width: 258px; height: 197px;
    background: linear-gradient(180deg, #496f36 0%, #5f8f3f 55%, #6fa14a 100%);
  }
  .welcome-crosses {
    position: absolute; left: 106px; top: 206px; width: 50px; height: 106px;
    background: linear-gradient(180deg, rgba(120,80,50,0.4), rgba(120,80,50,0.2));
  }
  .welcome {
    position: absolute; left: 0; top: 262px; width: 258px; text-align: center;
    font-size: 13.5px; line-height: 20px; font-weight: 700; color: var(--white);
  }
  .return-address {
    position: absolute; left: 295px; top: 32px; font-style: normal;
    font-size: 12.5px; line-height: 20px; color: var(--ink);
  }
  .stamp-box {
    position: absolute; left: 413px; top: 27px; width: 122px; height: 120px;
    border: 1px solid var(--rule);
  }
  .address-line {
    position: absolute; left: 295px; width: 240px; height: 1px; background: var(--rule);
  }
  .line-1 { top: 229px; }
  .line-2 { top: 263px; }
  .line-3 { top: 298px; }
  .line-4 { top: 332px; }
</style>
</head>
<body>
  <section class="card-front">
    <h1 class="title">Fall Festival &amp; Movie Night</h1>
    <p class="enjoy">Enjoy</p>
    <div class="offers">
      <p class="lead">FREE Food &amp; Drinks &amp;<br>Games start at 4:00 PM</p>
      <p class="detail">bounce house for kids,<br>corn toss game<br>and more . . .</p>
      <p class="movie">FREE Movie, featuring</p>
      <p class="movie-title">Rivers Still Run</p>
      <p class="movie-time">starts at 6:15 PM</p>
    </div>
    <div class="event-photo" role="img" aria-label="Photo of families enjoying a festival on a grassy park with tents and trees"></div>
    <div class="crosses" role="img" aria-label="Illustration of three wooden crosses"></div>
    <ul class="details">
      <li>Saturday, October 11, 2014</li>
      <li>4619 Marlow Lane, South Chesterfield, VA 23803,</li>
      <li class="cont">the future home of Brookhaven Fellowship Church</li>
      <li>Rain date on October 18, 2014</li>
    </ul>
    <p class="bring">Please bring lawn chairs and blankets<br>to watch a FREE outdoor movie</p>
  </section>

  <section class="card-back">
    <div class="welcome-panel">
      <div class="picnic-photo" role="img" aria-label="Photo of people sitting and talking on grass under shady trees"></div>
      <div class="welcome-crosses" role="img" aria-label="Illustration of three wooden crosses"></div>
      <p class="welcome">Welcome to the<br>Future Home of<br>Brookhaven Fellowship Church</p>
    </div>
    <address class="return-address">
      Brookhaven<br>Fellowship Church<br>4619 Marlow Lane<br>South Chesterfield<br>VA 23803
    </address>
    <div class="stamp-box"></div>
    <div class="address-line line-1"></div>
    <div class="address-line line-2"></div>
    <div class="address-line line-3"></div>
    <div class="address-line line-4"></div>
  </section>
</body>
</html>
```